Program Cover Design Project

I am the artistic director of a very successful music ensemble celebrating our 5th year anniversary season under my leadership. I hope to create a dynamic program cover for our 2013-2014 season concerts that incorporates our 5 year anniversary info.

I hope to have a cover that is simple, clean, and ties into our website (www.HAVRELnyc.com). We have three main groups of concerts for the year, and I hope to have an design that can be adapted to each group, so simplicity is important. We will likely just change colors, not design elements so that we retain a common theme for the year.

The cover will be folded to 8.5x11 in full color, and the design (in the above-described three variants) will be used for 25 concerts during our season, which means that over 6,500 people will see your design.

I am happy to connect about specifics!

Target Market(s)

Concertgoers

Industry/Entity Type

Leadership

Requirements
Must have
• -Our ensemble's logo
-The large 5 for our season and wording that accompanies it ("celebrating five years")
-File formatted in Adobe Photoshop, Illustrator, or Indesign

```html
<!DOCTYPE html>
<html lang="en">
<head>
<meta charset="utf-8">
<title>HAVREL — Celebrating Five Years — 2013–2014 Season Program</title>
<link rel="stylesheet" href="https://fonts.googleapis.com/css2?family=Cinzel:wght@400&family=Cormorant+Garamond:wght@500&family=Source+Sans+3:wght@400&display=swap">
<style>
  :root {
    --paper: #ffffff;
    --ghost: #f7f0ea;
    --crimson: #c1272d;
    --crimson-deep: #a8262a;
    --crimson-bright: #e0232a;
    --white: #ffffff;
  }
  html, body {
    margin: 0;
    padding: 0;
    width: 908px;
    height: 1200px;
    overflow: hidden;
    background: var(--paper);
  }
  .cover {
    position: relative;
    width: 908px;
    height: 1200px;
    overflow: hidden;
    background: var(--paper);
  }
  .ghost-numeral {
    position: absolute;
    left: -70px;
    top: -250px;
    margin: 0;
    font-family: "Cormorant Garamond", serif;
    font-weight: 500;
    font-size: 1380px;
    line-height: 1;
    color: var(--ghost);
    user-select: none;
  }
  .flame-motif {
    position: absolute;
    left: 612px;
    top: 145px;
    width: 278px;
    height: 760px;
    border-radius: 60% 40% 0 0 / 30% 20% 0 0;
    background: linear-gradient(160deg, var(--crimson-deep) 0%, var(--crimson-bright) 55%, var(--crimson) 100%);
    opacity: 0.9;
    filter: drop-shadow(-6px 8px 10px rgba(0,0,0,0.18));
  }
  .season-band {
    position: absolute;
    left: 797px;
    top: 900px;
    width: 93px;
    height: 254px;
    background: var(--crimson);
    box-shadow: -6px 8px 12px rgba(0,0,0,0.2);
    display: flex;
    align-items: flex-end;
    justify-content: center;
  }
  .season-years {
    margin: 0 0 22px;
    writing-mode: vertical-rl;
    transform: rotate(180deg);
    font-family: "Source Sans 3", sans-serif;
    font-size: 18px;
    letter-spacing: 0.22em;
    color: var(--white);
  }
  .anniversary {
    position: absolute;
    left: 0;
    top: 330px;
    width: 888px;
    text-align: center;
  }
  .anniversary-numeral {
    margin: 0;
    font-family: "Cinzel", serif;
    font-weight: 400;
    font-size: 330px;
    line-height: 1;
    color: var(--crimson);
    text-shadow: -4px 8px 10px rgba(0,0,0,0.15);
  }
  .anniversary-tagline {
    margin: 36px 0 0;
    font-family: "Source Sans 3", sans-serif;
    font-size: 19px;
    letter-spacing: 0.24em;
    color: var(--crimson);
  }
  .ensemble-name {
    position: absolute;
    left: 0;
    top: 1010px;
    width: 888px;
    margin: 0;
    text-align: center;
    font-family: "Cinzel", serif;
    font-weight: 400;
    font-size: 58px;
    letter-spacing: 0.08em;
    line-height: 1;
    color: var(--crimson);
  }
</style>
</head>
<body>
  <main class="cover">
    <p class="ghost-numeral" aria-hidden="true">5</p>

    <div class="flame-motif" role="img" aria-label="Red flowing flame ribbon motif rising from the season band"></div>

    <div class="season-band">
      <p class="season-years">2013–2014</p>
    </div>

    <section class="anniversary">
      <h1 class="anniversary-numeral">5</h1>
      <p class="anniversary-tagline">Celebrating five years</p>
    </section>

    <h2 class="ensemble-name">HAVREL</h2>
  </main>
</body>
</html>
```